Flyer Template

I need a flyer template for door knocking on properties. Text Boxes need to be editable, with a header and text body. Footer to be my info. Project to be stylized to match my real estate signs and logo art from past projects

```html
<!DOCTYPE html>
<html lang="en">
<head>
<meta charset="utf-8">
<title>Marlow Realty – Door Knocking Flyer</title>
<link rel="stylesheet" href="https://fonts.googleapis.com/css2?family=Lato:wght@400;700;900&family=Oswald:wght@500;700&display=swap">
<style>
  :root{
    --red:#e8403a;
    --red-deep:#d9322c;
    --black:#0d0d0d;
    --white:#ffffff;
    --panel:#e6e5e6;
    --canvas:#d7d7d7;
    --ink:#1b1b1b;
    --photo-sky:#6f8fb3;
    --photo-warm:#c98a3f;
  }
  *{margin:0;padding:0;box-sizing:border-box}
  html,body{width:1200px;height:1200px;overflow:hidden;background:var(--canvas)}
  .flyer{
    position:absolute;left:172px;top:50px;width:856px;height:1100px;
    background:var(--white);overflow:hidden;
    font-family:'Lato',sans-serif;color:var(--ink);
  }
  .abs{position:absolute}
  .hero-shapes{left:0;top:0;width:856px;height:568px}
  .lower-tint{left:0;top:568px;width:476px;height:360px;
    background:linear-gradient(160deg,#eeeeee 0%,#ffffff 70%)}

  .brand{left:0;top:40px;width:402px;text-align:center}
  .brand-square{width:34px;height:34px;background:var(--red);margin:0 auto 18px}
  .brand-name{font-family:'Lato',sans-serif;font-weight:900;font-size:25px;line-height:34px;color:var(--black);letter-spacing:.5px}

  .headline{left:24px;top:196px;color:var(--white);font-family:'Oswald',sans-serif;font-weight:700}
  .headline .lead{font-size:49px;line-height:60px;display:block}
  .headline .main{font-size:70px;line-height:72px;display:block;letter-spacing:.5px}
  .tag-box{left:23px;top:333px;width:374px;height:62px;background:var(--white);
    font-family:'Lato',sans-serif;font-weight:700;font-size:45px;line-height:62px;color:var(--black);padding-left:14px}
  .hero-copy{left:24px;top:405px;width:400px;font-size:16px;line-height:20px;color:var(--white)}

  .services-title{left:0;top:492px;width:360px;height:84px;background:var(--black);
    font-family:'Oswald',sans-serif;font-weight:700;font-size:48px;line-height:84px;color:var(--white);padding-left:22px}
  .service-list{list-style:none;font-size:15px;line-height:27.3px;color:var(--ink)}
  .service-list li{display:flex;align-items:center;gap:8px}
  .service-list li::before{content:"";width:9px;height:9px;border:2px solid var(--red);flex:none}
  .col-a{left:43px;top:585px}
  .col-b{left:265px;top:585px}
  .services-copy{left:37px;top:826px;width:400px;font-size:16px;line-height:20px;color:var(--ink)}

  .agent-panel{left:476px;top:568px;width:357px;height:339px;background:var(--panel)}
  .agent-portrait{left:493px;top:427px;width:320px;height:320px;border-radius:50%;
    border:4px solid var(--black);
    background:radial-gradient(circle at 50% 38%,#c9a58b 0 22%,#bfbfbd 23% 60%,#a9c3dd 61%)}
  .agent-name{left:476px;top:750px;width:357px;text-align:center;font-family:'Oswald',sans-serif;font-weight:500;font-size:48px;line-height:64px;color:var(--red)}
  .contact{left:546px;font-size:24px;line-height:30px;color:var(--black);display:flex;align-items:center;gap:10px}
  .contact-phone{top:822px}
  .contact-mail{top:855px}
  .contact svg{flex:none}

  .info-bar{left:23px;top:930px;width:810px;height:146px;background:var(--black);color:var(--white)}
  .info-col{position:absolute;top:20px}
  .info-col h3{font-family:'Oswald',sans-serif;font-weight:500;font-size:17px;line-height:22px;letter-spacing:.3px;margin-bottom:12px}
  .info-col p{font-size:12px;line-height:15px;width:190px}
  .col-about{left:54px}
  .col-features{left:332px;top:20px}
  .col-prices{left:622px;width:105px;text-align:center}
  .col-prices p{font-size:15px;line-height:26px;width:auto;margin-top:-4px}
  .divider{position:absolute;top:23px;width:2px;height:100px;background:var(--white);border-radius:1px}
  .divider-1{left:273px}
  .divider-2{left:558px}
  .base-band{left:0;top:1088px;width:856px;height:12px;background:var(--red)}
</style>
</head>
<body>
<main class="flyer">
  <svg class="abs hero-shapes" viewBox="0 0 856 568" aria-hidden="true">
    <defs>
      <linearGradient id="photoTone" x1="0" y1="0" x2="1" y2="1">
        <stop offset="0" stop-color="var(--photo-sky)"/>
        <stop offset=".55" stop-color="#8a8466"/>
        <stop offset="1" stop-color="var(--photo-warm)"/>
      </linearGradient>
      <linearGradient id="redTone" x1="0" y1="0" x2="1" y2="1">
        <stop offset="0" stop-color="var(--red)"/>
        <stop offset="1" stop-color="var(--red-deep)"/>
      </linearGradient>
    </defs>
    <rect x="0" y="0" width="856" height="568" fill="url(#photoTone)" role="img" aria-label="Photo of modern apartment buildings at dusk with a lit brick walkway"/>
    <polygon points="0,0 518,0 377,188 0,188" fill="var(--white)"/>
    <polygon points="0,188 377,188 530,472 856,472 856,568 0,568" fill="url(#redTone)" opacity=".93"/>
  </svg>
  <div class="abs lower-tint"></div>

  <div class="abs brand">
    <div class="brand-square"></div>
    <div class="brand-name">MARLOW<br>REALTY</div>
  </div>

  <h1 class="abs headline"><span class="lead">The First steps to</span><span class="main">HOME BUYING</span></h1>
  <div class="abs tag-box">LOREM IPSUM</div>
  <p class="abs hero-copy">Lorem ipsum dolor sit amet, consectetur adipiscing elit, sed do eiusmod tempor incididunt ut labore et dolore magna aliqua.</p>

  <h2 class="abs services-title">OUR SERVICES</h2>
  <ul class="abs service-list col-a">
    <li>Lorem ipsum</li>
    <li>dolor sit amet</li>
    <li>consectetur adipiscing elit</li>
    <li>sed do eiusmod tempor</li>
    <li>incididunt ut labore et</li>
    <li>dolore magna aliqua.</li>
    <li>Ut enim ad minim</li>
    <li>veniam, quis nostrud</li>
  </ul>
  <ul class="abs service-list col-b">
    <li>exercitation ullamco</li>
    <li>laboris nisi ut aliquip</li>
    <li>ex ea commodo consequat</li>
    <li>Duis aute irure dolor</li>
    <li>in reprehenderit in</li>
    <li>voluptate velit esse</li>
    <li>cillum dolore eu fugiat</li>
    <li>nulla pariatur</li>
  </ul>
  <p class="abs services-copy">Lorem ipsum dolor sit amet, consectetur adipiscing elit, sed do eiusmod tempor incididunt ut labore et dolore magna aliqua.</p>

  <div class="abs agent-panel"></div>
  <div class="abs agent-portrait" role="img" aria-label="Portrait photo of the agent"></div>
  <div class="abs agent-name">Jordan Marlow</div>
  <div class="abs contact contact-phone">
    <svg width="22" height="22" viewBox="0 0 22 22" aria-hidden="true"><circle cx="11" cy="11" r="10" fill="none" stroke="var(--red)" stroke-width="1.6"/><path d="M7.5 6.5c.8-.6 1.5-.4 2 .5l.6 1.3c.3.6 0 1-.5 1.4.6 1.3 1.5 2.2 2.8 2.8.4-.5.8-.8 1.4-.5l1.3.6c.9.5 1.1 1.2.5 2-1 1.2-2.7 1-4.6-.4-1.6-1.2-3-2.8-3.7-4.6-.6-1.4-.6-2.5.2-3.1z" fill="var(--red)"/></svg>
    <span>555-010-0147</span>
  </div>
  <div class="abs contact contact-mail">
    <svg width="22" height="16" viewBox="0 0 22 16" aria-hidden="true"><rect x="0" y="0" width="22" height="16" fill="var(--red)"/><path d="M1 1l10 8 10-8" fill="none" stroke="var(--white)" stroke-width="1.6"/></svg>
    <span>jmarlow@example.com</span>
  </div>

  <section class="abs info-bar">
    <div class="info-col col-about">
      <h3>ABOUT THE PROPERTY</h3>
      <p>Lorem ipsum dolor sit amet, consectetur adipiscing elit, sed do eiusmod tempor incididunt ut labore et dolore magna aliqua. Ut enim ad</p>
    </div>
    <div class="divider divider-1"></div>
    <div class="info-col col-features">
      <h3>PROPERTY FEATURES</h3>
      <p>Lorem ipsum dolor sit amet, consectetur adipiscing elit, sed do eiusmod tempor incididunt ut labore et dolore magna aliqua. Ut enim ad</p>
    </div>
    <div class="divider divider-2"></div>
    <div class="info-col col-prices">
      <h3>PRICES</h3>
      <p>$ 1,000.00<br>$ 2,000.00</p>
    </div>
  </section>
  <div class="abs base-band"></div>
</main>
</body>
</html>
```